Your After-Split Lantern: Sensible, Everyday Guidance for the Freshly Solo

I need a wraparound book cover design for a ~132-page workbook. Trim size will be 8.5x11 and the book will be on 60# paper. The name of this project is the name and subtitle of the book. Here's the synopsis I've come up with, which should be included on the back cover (without the quote marks):
"So you're divorced. What do you do now? There are probably a whole bunch of
things you never thought of, like:
- Cleaning up and automating your finances
- Making sure your insurance coverages are all correct
- Removing your former spouse's name from your assets and liabilities
- Building your personal team of financial advisors
Are you aware you need to take care of these things, but you don't know where to
start? This workbook is perfect for you. You'll be led, step by step, through detailed
explanations of how to do everything on this list, and much, much more!"
Here's the author bio for the back cover:
"Gregory T. Halvorsen, Esq. graduated from Brantwell College School of Law in 2002 and has been a practicing trial lawyer in the Metro Atlanta area ever since. Family law has always been a big part of Greg's practice. Throughout his career, Greg has helped hundreds of people through their divorce cases, and now through this book, Greg looks forward to being able to help them after the dust settles."
I have an ISBN bar code ready to go, so leave space for it on the back cover in the bottom right corner (winner will be expected to add the bar code graphic to the finished product).
This will be a print-on-demand book through Quillora's PressNest. They have a sizing template if you want to grab it for yourself.
Target Market(s)
Primarily divorced women, especially middle-aged and older

```html
<!DOCTYPE html>
<html lang="en">
<head>
<meta charset="utf-8">
<title>Your After-Split Lantern – Wraparound Cover</title>
<link rel="stylesheet" href="https://fonts.googleapis.com/css2?family=Anton&family=Lora:wght@400&display=swap">
<style>
  :root {
    --cover-red: #ec1c24;
    --ink: #111111;
    --paper: #ffffff;
    --spine-text: #ffffff;
  }
  * { margin: 0; padding: 0; box-sizing: border-box; }
  html, body { width: 1200px; height: 776px; overflow: hidden; background: var(--paper); }
  .cover { position: relative; width: 1200px; height: 776px; background: var(--paper); color: var(--ink); }

  /* Back cover */
  .back { position: absolute; left: 0; top: 0; width: 576px; height: 776px; }
  .back-hook {
    position: absolute; left: 20px; top: 31px; width: 520px;
    font-family: "Lora", serif; color: var(--cover-red);
    font-size: 16px; line-height: 26px; text-align: center; text-transform: uppercase;
  }
  .back-body {
    position: absolute; left: 47px; top: 127px; width: 454px;
    font-family: "Lora", serif; font-size: 15.6px; line-height: 22.3px; text-align: justify;
  }
  .back-body ul { list-style: none; text-align: left; }
  .bio-heading {
    position: absolute; left: 47px; top: 363px; width: 454px; text-align: center;
    font-family: "Anton", sans-serif; color: var(--cover-red); font-size: 32px; line-height: 40px; font-weight: 400;
  }
  .bio-body {
    position: absolute; left: 47px; top: 414px; width: 454px;
    font-family: "Lora", serif; font-size: 15.6px; line-height: 22.3px; text-align: justify;
  }

  /* Spine */
  .spine {
    position: absolute; left: 576px; top: 0; width: 45px; height: 776px;
    background: var(--cover-red); color: var(--spine-text);
  }
  .spine-title, .spine-author {
    position: absolute; left: 0; height: 45px; line-height: 45px;
    transform-origin: 0 0; transform: rotate(-90deg);
    white-space: nowrap; text-align: left;
  }
  .spine-title {
    top: 403px; width: 342px;
    font-family: "Anton", sans-serif; font-size: 19px; letter-spacing: 1.6px;
  }
  .spine-author {
    top: 713px; width: 290px;
    font-family: "Lora", serif; font-size: 25px;
  }

  /* Front cover */
  .front { position: absolute; left: 620px; top: 0; width: 580px; height: 776px; }
  .front-title { position: absolute; left: 0; top: 0; width: 580px; height: 280px; }
  .front-title text { font-family: "Anton", sans-serif; }
  .title-small, .title-main { fill: var(--ink); }
  .title-accent { fill: var(--cover-red); }
  .front-art {
    position: absolute; left: 60px; top: 272px; width: 258px; height: 351px;
    background: radial-gradient(circle at 45% 62%, rgba(227,38,44,0.55) 0 26%, rgba(255,255,255,0) 42%),
                linear-gradient(180deg, #eef0f6 0%, #f6e6e7 100%);
  }
  .front-subtitle {
    position: absolute; left: 300px; top: 318px; width: 260px; text-align: center;
    font-family: "Lora", serif; font-size: 37px; line-height: 55px; color: var(--ink);
  }
  .front-subtitle .accent { color: var(--cover-red); }
  .front-author {
    position: absolute; left: 33px; top: 690px; width: 520px; text-align: center;
    font-family: "Lora", serif; font-size: 35px; line-height: 48px; color: var(--ink);
  }
</style>
</head>
<body>
<div class="cover">

  <section class="back">
    <p class="back-hook">So you're divorced. What do you do now?<br>There are probably a whole bunch of<br>things you never thought of, like:</p>
    <div class="back-body">
      <ul>
        <li>- Cleaning up and automating your finances</li>
        <li>- Making sure your insurance coverages are all correct</li>
        <li>- Removing your former spouse's name from your assets and liabilities.</li>
        <li>- Building your personal team of financial advisors</li>
      </ul>
      <p>Are you aware you need to take care of these things, but you don't know where to start? This workbook is perfect for you. You'll be led, step by step, through detailed explanations of how to do everything on this list, and much, much more.</p>
    </div>
    <h2 class="bio-heading">ABOUT THE AUTHOR</h2>
    <p class="bio-body">Gregory T. Halvorsen, Esq. graduated from Brantwell College School of Law in 2002 and has been a practicing trial lawyer in the Metro Atlanta area ever since. Family law has always been a big part of Greg's practice. Throughout his career, Greg has helped hundreds of people through their divorce cases, and now through this book, Greg looks forward to being able to help them after the dust settles.</p>
  </section>

  <aside class="spine">
    <div class="spine-title">YOUR AFTER-SPLIT LANTERN</div>
    <div class="spine-author">Gregory T. Halvorsen</div>
  </aside>

  <section class="front">
    <svg class="front-title" viewBox="0 0 580 280" aria-label="Your After-Split Lantern">
      <text class="title-small" x="255" y="64" font-size="29" textLength="73" lengthAdjust="spacingAndGlyphs">YOUR</text>
      <text class="title-main" x="32" y="159" font-size="96" textLength="520" lengthAdjust="spacingAndGlyphs">AFTER-SPLIT</text>
      <text class="title-accent" x="76" y="258" font-size="110" textLength="431" lengthAdjust="spacingAndGlyphs">LANTERN</text>
    </svg>

    <div class="front-art" role="img" aria-label="Illustration: gavel, house, cars and family figures around a red and blue sphere of dollar signs"></div>

    <p class="front-subtitle">Sensible,<br>Everyday<br>Guidance for<br><span class="accent">the Freshly<br>Solo</span></p>

    <p class="front-author">Gregory T. Halvorsen</p>
  </section>

</div>
</body>
</html>
```